Flyer-Design für die Gleichstellungsstelle einer kommunalen Stadtverwaltung
Zielgruppe
Wir sind die Gleichstellungsstelle einer kommunalen Stadtverwaltung (Einwohner*innen ca. 74.500) und richten uns mit unserer Arbeit grundsätzlich an alle Menschen. Wir möchten einen übersichtlichen Flyer haben, der die wichtigsten Rahmenbedingungen unserer Arbeit erläutert und Kontaktdaten enthält (z.B. sollen neue Mitarbeiter*innen der Verwaltung den Flyer erhalten).
Aufgabenstellung
- Der Flyer soll im Format DIN A6 sein, die Rückseite (Text) im Hochformat, die Vorderseite kann im Hoch- oder Querformat sein.
- Die Vorderseite soll gestaltet werden. Die Auswahl / Gestaltung liegt in der Kreativität der Designer*innen.
- Das Bild auf der Vorderseite kann auch eine Wortwolke kann, muss aber nicht! Begriffe für eine mögliche Wortwolke sind in an angehängten Dateien zu finden.
- Auf der Rückseite muss das angehängte Logo der Gleichstellungsstelle gemäß Corporate Design enthalten sein.
- Außer bei Fotos ist möglichst auf die Farbwelt des Corporate Designs zu achten.
- Schriftart gemäß Corporate Design (wenn möglich Avenir Next, alternativ Arial oder ähnliche Schrift).

```html
<!DOCTYPE html>
<html lang="de">
<head>
<meta charset="utf-8">
<title>Gleichstellungsstelle – Flyer Vorderseite</title>
<link rel="stylesheet" href="https://fonts.googleapis.com/css2?family=Nunito+Sans:wght@400;500;600;700;800&display=swap">
<style>
  :root {
    --rose: #d47f7f;
    --rose-deep: #8a3d3c;
    --white: #ffffff;
    --tone-maroon: #7a3236;
    --tone-slate: #7f9aa0;
    --tone-plum: #5f5568;
    --tone-skin: #b8704f;
    --tone-teal: #4e8a8c;
    --tone-coral: #c65d5d;
  }
  html, body {
    margin: 0;
    padding: 0;
    width: 1200px;
    height: 851px;
    overflow: hidden;
    background: var(--rose);
  }
  .flyer-front {
    position: relative;
    width: 1200px;
    height: 851px;
    background: var(--rose);
    overflow: hidden;
    font-family: "Nunito Sans", "Avenir Next", Arial, sans-serif;
  }
  .quote {
    position: absolute;
    top: 96px;
    left: 0;
    width: 1186px;
    margin: 0;
    text-align: center;
    color: var(--white);
    font-weight: 500;
    font-size: 54px;
    line-height: 70px;
    letter-spacing: 0.3px;
    text-transform: uppercase;
  }
  .quote .highlight {
    color: var(--rose-deep);
    font-weight: 700;
  }
  .quote-author {
    position: absolute;
    top: 320px;
    left: 752px;
    margin: 0;
    color: var(--white);
    font-weight: 400;
    font-size: 26px;
    letter-spacing: 0.3px;
  }
  .crowd-illustration {
    position: absolute;
    left: 0;
    top: 455px;
    width: 1200px;
    height: 396px;
    background:
      linear-gradient(180deg, rgba(212,127,127,0.55) 0%, rgba(212,127,127,0) 35%),
      linear-gradient(90deg,
        var(--tone-maroon) 0%,
        var(--tone-slate) 22%,
        var(--tone-plum) 40%,
        var(--tone-skin) 56%,
        var(--tone-teal) 68%,
        var(--tone-maroon) 80%,
        var(--tone-coral) 100%);
  }
</style>
</head>
<body>
  <main class="flyer-front">
    <p class="quote">
      Es wird keine<br>
      <span class="highlight">Gleichberechtigung</span> geben,<br>
      solange alles gleich bleibt.
    </p>
    <p class="quote-author">Selin Arvak</p>
    <div class="crowd-illustration" role="img" aria-label="Flache Illustration einer vielfältigen Gruppe von Menschen unterschiedlicher Herkunft, nebeneinander stehend"></div>
  </main>
</body>
</html>
```